Reed & Vale NC grand opening (for BILLBOARD)

Advertising the grand opening of our cannabis/hemp shop in NC. We will sell all things hemp (flower, cartridges, disposables, edibles, creams, lotions, pet products etc...)

Requirements
Must have
• include, open starting Aug 1, but grand opening Aug 15th.
Nice to have
• Difference slogan ideas "Save some cash, buy our grass" "Find your perfect high at Reed & Vale cannabis store" "Experience Nature's Gift: Reed & Vale Cannabis Store"

```html
<!DOCTYPE html>
<html lang="en">
<head>
<meta charset="utf-8">
<title>Reed &amp; Vale Grand Opening Billboard</title>
<link rel="stylesheet" href="https://fonts.googleapis.com/css2?family=Josefin+Sans:wght@400;600;700&family=Lobster+Two:ital,wght@1,700&family=Montserrat:wght@300;400;800&display=swap">
<style>
  :root {
    --backdrop: #dcdadb;
    --paper: #ffffff;
    --leaf-green: #86bc3c;
    --leaf-green-deep: #74a82f;
    --ink: #1c1c1c;
    --navy: #1a1935;
    --white: #ffffff;
  }
  * { margin: 0; padding: 0; box-sizing: border-box; }
  html, body {
    width: 1200px;
    height: 1200px;
    overflow: hidden;
    background: var(--backdrop);
  }
  .billboard {
    position: absolute;
    left: 78px;
    top: 338px;
    width: 1045px;
    height: 522px;
    background: var(--paper);
    overflow: hidden;
    font-family: "Josefin Sans", sans-serif;
    color: var(--ink);
  }
  .smoke-field {
    position: absolute;
    inset: 0;
    width: 100%;
    height: 100%;
  }
  .smoke-field .cloud { fill: var(--leaf-green); }
  .smoke-field .wisp {
    fill: none;
    stroke: var(--leaf-green-deep);
    stroke-width: 1.6;
  }
  .brand-name {
    position: absolute;
    left: 54px;
    top: 82px;
    font-size: 64px;
    font-weight: 600;
    color: var(--leaf-green);
    letter-spacing: -0.5px;
    line-height: 1;
  }
  .slogan {
    position: absolute;
    left: 54px;
    top: 196px;
    font-size: 26px;
    line-height: 37px;
    font-weight: 400;
  }
  .product-list {
    position: absolute;
    left: 54px;
    top: 348px;
  }
  .product-list h2 {
    font-size: 24px;
    font-weight: 700;
    line-height: 30px;
  }
  .product-list ul {
    list-style: none;
    font-size: 20px;
    line-height: 29px;
  }
  .opening-info {
    position: absolute;
    left: 600px;
    top: 0;
    width: 410px;
    text-align: center;
  }
  .soft-open {
    position: absolute;
    left: 0;
    right: 0;
    top: 64px;
    font-size: 31px;
    font-weight: 400;
    color: var(--ink);
  }
  .grand-opening {
    position: absolute;
    left: 0;
    right: 0;
    top: 164px;
    color: var(--white);
    font-family: "Montserrat", sans-serif;
  }
  .grand-opening .grand {
    display: block;
    font-size: 70px;
    font-weight: 800;
    line-height: 66px;
  }
  .grand-opening .opening {
    display: block;
    font-size: 68px;
    font-weight: 400;
    line-height: 62px;
    letter-spacing: 1px;
  }
  .grand-date {
    position: absolute;
    left: 0;
    right: 26px;
    top: 290px;
    font-family: "Lobster Two", cursive;
    font-style: italic;
    font-weight: 700;
    font-size: 62px;
    color: var(--ink);
  }
</style>
</head>
<body>
  <section class="billboard">
    <svg class="smoke-field" viewBox="0 0 836 418" preserveAspectRatio="none" aria-hidden="true">
      <path class="cloud" d="M 383 418
        C 410 398, 440 382, 452 360
        A 22 22 0 0 1 440 330
        A 24 24 0 0 1 432 290
        A 22 22 0 0 1 440 252
        A 24 24 0 0 1 470 212
        C 492 188, 470 150, 456 120
        C 446 100, 452 88, 460 76
        A 20 20 0 0 1 420 72
        A 22 22 0 0 1 374 56
        A 24 24 0 0 1 392 20
        A 22 22 0 0 1 424 14
        C 432 6, 438 0, 442 0
        L 836 0 L 836 418 Z"/>
      <path class="wisp" d="M 684 418 C 690 330, 730 260, 790 220 C 830 190, 836 150, 836 120"/>
      <path class="wisp" d="M 452 360 C 560 300, 600 240, 640 170 C 680 100, 760 120, 836 100"/>
    </svg>

    <div class="brand-name">Reed &amp; Vale</div>

    <p class="slogan">Find your perfect high at<br>Reed &amp; Vale cannabis store</p>

    <div class="product-list">
      <h2>We will sell all things hemp</h2>
      <ul>
        <li>• Flower • Cartridges</li>
        <li>• Disposables • Edibles</li>
        <li>• Creams • lotions • pet products etc...)</li>
      </ul>
    </div>

    <div class="opening-info">
      <p class="soft-open">Open starting Aug 1st</p>
      <h1 class="grand-opening">
        <span class="grand">Grand</span>
        <span class="opening">Opening</span>
      </h1>
      <p class="grand-date">Aug 15th</p>
    </div>
  </section>
</body>
</html>
```